Geschäftspapiere für Hersteller von Werkstattausrüstung
Zielgruppe
Werkstattausrüstung (Hebebühnen, Achsmessgeräte, Wuchtmaschinen etc.) Zielgruppe Kfz Werkstätte

```html
<!DOCTYPE html>
<html lang="de">
<head>
<meta charset="utf-8">
<title>Holm &amp; Brenner – Geschäftspapiere</title>
<link href="https://fonts.googleapis.com/css2?family=Source+Sans+3:wght@300;400;600;700&display=swap" rel="stylesheet">
<style>
  :root {
    --bg: #e4e4e4;
    --paper: #ffffff;
    --green-dark: #006f52;
    --green-light: #8aba24;
    --text: #2a2a2a;
    --ink: #1f2a8a;
  }
  * { margin: 0; padding: 0; box-sizing: border-box; }
  html, body { width: 1200px; height: 1200px; overflow: hidden; }
  body { background: var(--bg); font-family: "Source Sans 3", sans-serif; position: relative; }

  .sheet {
    position: absolute; top: 261px; width: 480px; height: 678px;
    background: var(--paper); box-shadow: 2px 2px 4px rgba(0,0,0,.22);
  }
  .sheet--blank { left: 99px; }
  .sheet--letter { left: 621px; }

  .edge-band { position: absolute; left: 0; top: 0; width: 15px; height: 100%; background: var(--green-dark); }
  .edge-band::before { content: ""; position: absolute; left: 0; top: 0; width: 100%; height: 239px; background: var(--green-light); }
  .edge-band::after { content: ""; position: absolute; left: 0; top: 338px; width: 100%; height: 1px; background: var(--paper); }

  .brand { position: absolute; left: 119px; top: 28px; display: flex; align-items: center; gap: 10px; }
  .brand-dot { width: 48px; height: 48px; border-radius: 50%; background: var(--green-dark); }
  .brand-name { font-weight: 700; font-size: 25px; line-height: 1; color: var(--green-dark); letter-spacing: .5px; }
  .brand-tagline { font-weight: 400; font-size: 16px; color: var(--green-dark); margin-top: 3px; }

  .sender-line { position: absolute; left: 53px; top: 112px; font-size: 4.6px; color: var(--green-light); display: flex; align-items: center; gap: 3px; white-space: nowrap; }
  .sender-line .dot { width: 7px; height: 7px; border-radius: 50%; background: var(--green-dark); }
  .sender-line strong { color: var(--green-dark); font-weight: 700; }

  .letter { position: absolute; left: 53px; width: 400px; color: var(--text); font-size: 7.4px; font-weight: 300; line-height: 10.2px; }
  .letter-date { position: absolute; right: 24px; top: 252px; font-size: 7.4px; font-weight: 300; color: var(--text); }
  .letter-subject { top: 282px; font-weight: 700; font-size: 7.6px; color: #000; }
  .letter-salutation { top: 322px; }
  .letter-body { top: 342px; }
  .letter-body p + p { margin-top: 10.2px; }
  .letter-closing { top: 476px; }
  .letter-signature { position: absolute; left: 53px; top: 496px; width: 100px; height: 22px; background: linear-gradient(90deg, rgba(31,42,138,.18), rgba(31,42,138,.06)); border-radius: 3px; }
  .letter-name { top: 529px; }

  .footer { position: absolute; left: 53px; top: 630px; display: flex; align-items: flex-start; font-size: 4.5px; line-height: 7.3px; color: var(--green-light); white-space: nowrap; }
  .footer-mark { width: 34px; height: 24px; margin-right: 13px; display: flex; align-items: center; }
  .footer-mark span { width: 22px; height: 22px; border-radius: 50%; background: var(--green-dark); }
  .footer-col { border-left: .6px solid var(--green-dark); padding: 0 4px; }
  .footer-col b { color: var(--green-dark); font-weight: 700; display: inline-block; }
  .footer-col--company { width: 87px; }
  .footer-col--contact { width: 82px; }
  .footer-col--contact b { width: 22px; }
  .footer-col--register { width: 106px; }
  .footer-col--register b { width: 42px; }
  .footer-col--bank b { width: 14px; }
</style>
</head>
<body>

<section class="sheet sheet--blank">
  <div class="edge-band"></div>
  <div class="brand">
    <div class="brand-dot"></div>
    <div>
      <div class="brand-name">HOLM &amp; BRENNER</div>
      <div class="brand-tagline">Service | Werkstatt | Technik</div>
    </div>
  </div>
  <div class="sender-line"><span class="dot"></span><strong>HOLM &amp; BRENNER GmbH &amp; Co. KG</strong> • Talstraße 14 • 61234 Feldheim</div>
  <footer class="footer">
    <div class="footer-mark"><span></span></div>
    <div class="footer-col footer-col--company"><b>HOLM &amp; BRENNER GMBH &amp; CO. KG</b><br>Talstraße 14<br>61234 Feldheim</div>
    <div class="footer-col footer-col--contact"><b>Telefon:</b> +49 (0) 6100 / 123 45 0<br><b>E-Mail:</b> info@holm-brenner.de<br><b>Internet:</b> www.holm-brenner.de</div>
    <div class="footer-col footer-col--register"><b>Registergericht:</b> Amtsgericht Feldheim<br><b>Registernummer:</b> HRA 10427<br><b>USt-IdNr.</b> DE123456789</div>
    <div class="footer-col footer-col--bank"><b>Bank:</b> Muster Bank<br><b>IBAN:</b> DE12 3004 5607 0008 9911 12<br><b>BIC:</b> ABCDEFGH</div>
  </footer>
</section>

<section class="sheet sheet--letter">
  <div class="edge-band"></div>
  <div class="brand">
    <div class="brand-dot"></div>
    <div>
      <div class="brand-name">HOLM &amp; BRENNER</div>
      <div class="brand-tagline">Service | Werkstatt | Technik</div>
    </div>
  </div>
  <div class="sender-line"><span class="dot"></span><strong>HOLM &amp; BRENNER GmbH &amp; Co. KG</strong> • Talstraße 14 • 61234 Feldheim</div>

  <div class="letter-date">Musterstadt, 18.04.2022</div>
  <div class="letter letter-subject">Ich bin eine Betreffzeile mit Blindtext. Ich bin eine Betreffzeile mit Blindtext.</div>
  <div class="letter letter-salutation">Sehr geehrte Damen und Herren,</div>
  <div class="letter letter-body">
    <p>ich bin Blindtext. Von Geburt an. Es hat lange gedauert, bis ich begriffen habe, was es bedeutet, ein blinder Text zu sein: Man macht keinen Sinn. Man wirkt hier und da aus dem Zusammenhang gerissen. Oft wird man gar nicht erst gelesen. Aber bin ich deshalb ein schlechter Text? Ich weiß, dass ich nie die Chance haben werde im Stern zu erscheinen. Aber bin ich darum weniger wichtig? Ich bin blind! Aber ich bin gerne Text. Und sollten Sie mich jetzt tatsächlich zu Ende lesen, dann habe ich etwas geschafft, was den meisten „normalen“ Texten nicht gelingt. Ich bin Blindtext.</p>
    <p>Und sollten Sie mich jetzt tatsächlich zu Ende lesen, dann habe ich etwas geschafft, was den meisten „normalen“ Texten nicht gelingt. Ich bin Blindtext. Von Geburt an. Es hat lange gedauert, bis ich begriffen habe, was es bedeutet, ein blinder Text zu sein: Man macht keinen Sinn. Man wirkt hier und da aus dem Zusammenhang gerissen. Oft wird man gar nicht erst gelesen. Aber bin ich deshalb ein schlechter Text? Ich weiß, dass ich nie die Chance haben werde im Stern zu erscheinen. Aber bin ich darum weniger wichtig? Ich bin blind! Aber ich bin gerne Text. Und sollten Sie mich jetzt tatsächlich zu Ende lesen, dann habe ich etwas geschafft, was den meisten „normalen“ Texten nicht gelingt.</p>
  </div>
  <div class="letter letter-closing">Mit freundlichen Grüßen</div>
  <div class="letter-signature" role="img" aria-label="Handschriftliche Unterschrift in blauer Tinte"></div>
  <div class="letter letter-name">Max Mustermann</div>

  <footer class="footer">
    <div class="footer-mark"><span></span></div>
    <div class="footer-col footer-col--company"><b>HOLM &amp; BRENNER GMBH &amp; CO. KG</b><br>Talstraße 14<br>61234 Feldheim</div>
    <div class="footer-col footer-col--contact"><b>Telefon:</b> +49 (0) 6100 / 123 45 0<br><b>E-Mail:</b> info@holm-brenner.de<br><b>Internet:</b> www.holm-brenner.de</div>
    <div class="footer-col footer-col--register"><b>Registergericht:</b> Amtsgericht Feldheim<br><b>Registernummer:</b> HRA 10427<br><b>USt-IdNr.</b> DE123456789</div>
    <div class="footer-col footer-col--bank"><b>Bank:</b> Muster Bank<br><b>IBAN:</b> DE12 3004 5607 0008 9911 12<br><b>BIC:</b> ABCDEFGH</div>
  </footer>
</section>

</body>
</html>
```